BrightHarbor Web Design Project

BrightHarbor IT solutions, a IT mananaged services company is looking to redesign current website (brightharborsolutions.example).

The website should convey professionalism within the managed it services community. The layout should invite users to explore other areas of the site. Should contain tools and other current information that clients or potential clients would find useful. Product pages, special offers and informational pages should be easily editable by non-programmers. Tidewardnet.example is a good site to review as an example of the design components we like.

Target Market(s)

Professional services companies with 10-100 users

Industry/Entity Type

It Company

Requirements
Must have
• • Clickable icons and graphics are good
• SEO - Wordpress could be a great platform for us to work from as we already have internal experience with it and it’s easy to update. If not Wordpress, we would need something that is easy to SEO optimize
• An “our team” section with pictures
• Sell the message to potential clients why they need managed services
• Home page needs to convey our core services at a glance
• Home page needs to load quickly
• Screenshots of our monitoring and security reports
• Easy for us to update/edit certain areas
o New products
o Testimonials
Nice to have
• • Something like TN’s savings calculator - http://www.tidewardnet.example/it-savings-calculator/
• Webform to enter service ticket requests
• Motion of home page banner
• Maybe pull in RSS feeds from current tech news sources
• Rotating content on all pages to keep it fresh
• “Harbor-up” feature for monthly promos
Should not have
• • Should not be overly "techie" in feel.
• Not overly wordy (like current site)

```html
<!DOCTYPE html>
<html lang="en">
<head>
<meta charset="utf-8">
<title>BrightHarbor IT Solutions</title>
<link href="https://fonts.googleapis.com/css2?family=Ubuntu:wght@400;500;700&family=Arimo:wght@400;700&display=swap" rel="stylesheet">
<style>
:root{
  --green:#7fc31c;
  --green-dark:#5a9a0a;
  --green-light:#a9dc3a;
  --ink:#222;
  --text:#333;
  --muted:#555;
  --gray-card:#555;
  --gray-card-dark:#3a3a3a;
  --page:#fff;
  --outer:#e9e9e9;
}
*{box-sizing:border-box;margin:0;padding:0}
html,body{width:960px;height:1200px;overflow:hidden}
body{position:relative;background:linear-gradient(#fff 0,#fff 140px,var(--outer) 140px);font-family:"Arimo",Arial,sans-serif;color:var(--text)}
.abs{position:absolute}
.column{position:absolute;left:82px;top:0;width:796px;height:1044px;background:var(--page)}
/* header */
.brand{left:104px;top:10px;display:flex;align-items:center;gap:8px}
.brand-mark{width:34px;height:34px;border-radius:50%;background:var(--green)}
.brand-name{font-family:"Ubuntu",sans-serif;font-weight:500;font-size:20px;color:var(--green-dark);line-height:1}
.brand-tag{left:124px;top:58px;font-family:"Ubuntu",sans-serif;font-size:9px;letter-spacing:1px;color:var(--ink);font-weight:500}
.call{left:605px;top:8px;display:flex;gap:10px}
.call-label{font-family:"Ubuntu",sans-serif;font-size:13px;color:#777}
.call-num{font-family:"Ubuntu",sans-serif;font-size:14px;color:#444;margin-top:2px}
.follow{left:693px;top:74px;display:flex;align-items:center;gap:8px}
.follow-label{font-family:"Ubuntu",sans-serif;font-weight:700;font-size:16px;color:#999;margin-right:8px}
.social{width:24px;height:24px;border-radius:50%;background:radial-gradient(circle at 40% 35%,var(--green-light),var(--green-dark));box-shadow:0 2px 3px rgba(0,0,0,.25)}
/* nav */
.nav{left:72px;top:107px;width:816px;height:26px;display:flex;background:linear-gradient(var(--green-light),var(--green) 60%,var(--green-dark))}
.nav a{display:flex;align-items:center;justify-content:center;color:#fff;text-decoration:none;font-size:10.5px;border-right:1px solid rgba(255,255,255,.55)}
.nav a:last-child{border-right:none}
.nav-shade{left:72px;top:133px;width:816px;height:7px;background:#3d3d3d}
/* hero */
.hero{left:82px;top:140px;width:796px;height:266px;background:linear-gradient(90deg,#f7f7f7,#ececec)}
.hero-photo{left:96px;top:152px;width:352px;height:254px;background:linear-gradient(#e6e6e6,#cfcfcf 60%,#bfbfbf);border-radius:4px 4px 0 0}
.hero-title{left:470px;top:160px;width:390px;font-family:"Ubuntu",sans-serif;font-size:18px;line-height:24px;color:#666}
.hero-title b{color:var(--green-dark);font-weight:700}
.hero-copy{left:470px;top:248px;width:378px;font-size:9px;line-height:16px;color:#333;letter-spacing:.2px}
.hero-copy b{color:#111}
.btn-start{left:472px;top:349px;width:131px;height:35px;border-radius:9px;background:linear-gradient(#5a5a5a,#2c2c2c);border:2px solid #ddd;box-shadow:0 2px 3px rgba(0,0,0,.3);color:#fff;font-family:"Ubuntu",sans-serif;font-weight:700;font-size:16px;display:flex;align-items:center;justify-content:center;letter-spacing:.5px}
.dots{left:716px;top:384px;width:140px;height:28px;background:linear-gradient(var(--green-light),var(--green-dark));display:flex;align-items:center;justify-content:center;gap:9px}
.dots i{width:13px;height:13px;border-radius:50%;background:#fff}
.hero-base{left:82px;top:406px;width:796px;height:20px;background:linear-gradient(#ddd,#fff)}
/* section headings */
.ico{width:26px;height:26px;border-radius:50%;background:radial-gradient(circle at 40% 35%,var(--green-light),var(--green-dark));box-shadow:0 2px 3px rgba(0,0,0,.2);display:flex;align-items:center;justify-content:center;flex:none}
.ico i{width:10px;height:10px;background:#fff;border-radius:2px}
.sec-head{display:flex;align-items:center;gap:8px;font-family:"Ubuntu",sans-serif;font-size:16px;color:#555;border-bottom:1px dotted #ccc;padding-bottom:2px}
.sec-head b{color:#555;font-weight:500}
.sec-head .hl{color:var(--green-dark);font-weight:700}
.body-text{font-size:9px;line-height:14.4px;color:#333;letter-spacing:.2px}
.body-text b{color:#111}
.more{font-size:10px;color:#444}
/* welcome */
.welcome-head{left:86px;top:446px;width:300px}
.welcome-art{left:88px;top:488px;width:208px;height:176px;background:linear-gradient(120deg,#f2f2f2,#d9dde4 50%,#eaeaea)}
.welcome-text{left:296px;top:482px;width:311px}
.welcome-text p{margin-bottom:14.4px}
.welcome-more{left:541px;top:648px}
.team{left:634px;top:445px;width:238px;height:221px;border-radius:8px;background:linear-gradient(#fff,#eee);border:1px solid #e0e0e0}
.team-head{left:644px;top:450px;width:104px}
.team-photo{left:645px;top:484px;width:217px;height:89px;background:linear-gradient(#f3f3f3,#e1e5ea);border:4px solid #e6e6e6}
.team-text{left:645px;top:580px;width:216px;text-align:justify}
.team-more{left:797px;top:645px}
.divider{left:90px;top:684px;width:776px;border-top:1px dotted #ccc}
/* service cards */
.card{top:703px;width:248px;height:110px;border-radius:8px;padding:10px 12px;color:#fff}
.card.green{background:linear-gradient(var(--green-light),var(--green) 45%,var(--green-dark))}
.card.dark{background:linear-gradient(#6a6a6a,var(--gray-card) 40%,var(--gray-card-dark))}
.card-head{display:flex;align-items:center;gap:8px;font-family:"Ubuntu",sans-serif;font-size:16px;margin-bottom:9px;border-bottom:1px solid rgba(255,255,255,.3);padding-bottom:2px}
.card-head .ico{background:radial-gradient(circle at 40% 35%,#fff,#bbb)}
.card-head .ico i{background:#666}
.card p{font-size:9px;line-height:16px;letter-spacing:.2px;padding-left:0}
.card-corner{position:absolute;right:0;bottom:0;width:26px;height:26px;background:#fff;border-radius:26px 0 8px 0}
.card-corner:after{content:"";position:absolute;left:9px;top:9px;border-left:8px solid transparent;border-bottom:8px solid #555}
/* lists */
.col-head{top:858px;width:254px}
.list{top:890px;list-style:none;font-size:9.5px;letter-spacing:.3px;color:#333}
.list li{height:17.6px;display:flex;align-items:center;gap:10px}
.list li:before{content:"";width:10px;height:10px;border-radius:50%;border:1px solid #bbb;background:radial-gradient(circle,#6a9fd4 25%,#fff 30%)}
.list li.link{color:var(--green-dark);text-decoration:underline}
.report{left:626px;top:890px;width:229px;height:112px;background:linear-gradient(90deg,#eef1f5 0,#e4e9ef 35%,var(--green) 40%,var(--green-dark))}
.vline{top:886px;width:1px;height:130px;background:linear-gradient(#fff,#e2e2e2,#fff)}
/* footer */
.footer{left:72px;top:1044px;width:816px;height:156px;background:linear-gradient(var(--green-light),var(--green) 40%,var(--green-dark));border-top:6px solid #3d3d3d}
.foot-col{top:1064px;color:#fff}
.foot-col h4{font-size:9.5px;font-weight:700;letter-spacing:.3px;margin-bottom:6px}
.foot-col a{display:block;color:#fff;text-decoration:none;font-size:9.3px;letter-spacing:.4px;line-height:16px;padding-left:2px}
.testi-head{left:606px;top:1052px;display:flex;align-items:center;gap:6px;font-family:"Ubuntu",sans-serif;font-size:16px;color:#fff;border-bottom:1px dotted rgba(255,255,255,.5);width:166px}
.testi-head .ico{background:radial-gradient(circle at 40% 35%,#f7a44a,#2b6cb0)}
.testi{left:600px;top:1086px;width:244px;height:88px;border-radius:8px;background:rgba(255,255,255,.18);padding:7px 12px;color:#fff;font-size:9px;line-height:14.4px;text-align:justify;letter-spacing:.2px}
.testi:after{content:"";position:absolute;left:38px;bottom:-14px;border-left:10px solid transparent;border-top:14px solid rgba(255,255,255,.18)}
</style>
</head>
<body>
<div class="column"></div>

<header>
  <div class="abs brand"><span class="brand-mark"></span><span class="brand-name">BrightHarbor</span></div>
  <div class="abs brand-tag">IT SOLUTIONS</div>
  <div class="abs call">
    <svg width="32" height="38" viewBox="0 0 32 38" aria-hidden="true"><path d="M6 3c3-2 6 5 4 8-1 2 1 8 6 13 3 3 5 2 6 1 3-1 8 4 5 6-4 4-12 3-19-6S2 7 6 3z" fill="#8cc63f"/></svg>
    <div><div class="call-label">Call Today</div><div class="call-num">(888) 555-0142, (480) 555-0187</div></div>
  </div>
  <div class="abs follow"><span class="follow-label">Follow us</span><span class="social" aria-label="Social profile"></span><span class="social" aria-label="Social profile"></span><span class="social" aria-label="Social profile"></span></div>
</header>

<nav class="abs nav">
  <a style="width:89px">Home</a><a style="width:105px">Solutions</a><a style="width:105px">About Us</a><a style="width:106px">ContactIT</a><a style="width:122px">Consulting IT</a><a style="width:123px">Programs IT</a><a style="width:166px">Security Data Backup</a>
</nav>
<div class="abs nav-shade"></div>

<section>
  <div class="abs hero"></div>
  <div class="abs hero-photo" role="img" aria-label="Photo of two business colleagues reviewing a document"></div>
  <h1 class="abs hero-title"><b>BrightHarbor can help</b> your business harness the power of new technology, making your <b>business fast and efficient.</b></h1>
  <p class="abs hero-copy"><b>In the information age of today, one must stay abreast of current technology in order to thrive. New advancements are made</b> daily in dispersing information and collaborative computing. High-speed networks aid in the exchange of electronic information between businesses, their customers, vendors, and peers. Businesses that are quick to act and effectively implement this technology will rise to the top.</p>
  <div class="abs btn-start">START NOW</div>
  <div class="abs dots"><i></i><i></i><i></i><i></i><i></i></div>
  <div class="abs hero-base"></div>
</section>

<section>
  <h2 class="abs sec-head welcome-head"><span class="ico"><i></i></span><span>Welcome to <span class="hl">BrightHarbor</span> <b>IT Solution</b></span></h2>
  <div class="abs welcome-art" role="img" aria-label="Illustration of a businesswoman at a transparent data display"></div>
  <div class="abs welcome-text body-text">
    <p><b>BrightHarbor's company mission is to help small and mid-sized businesses properly plan and align</b> technology with critical business objectives, thereby maximizing efficiencies while leveraging new and existing technologies to maintain a competitive advantage.</p>
    <p>Our specific service offerings including information technology planning, consulting, project management/implementation, data backup and recovery, security management.</p>
    <p><b>Today, the growing team of technology</b> professionals at BrightHarbor continues to serve many of our original clients.</p>
  </div>
  <a class="abs more welcome-more">Read More »</a>

  <div class="abs team"></div>
  <h2 class="abs sec-head team-head"><span class="ico"><i></i></span><span>Our <b>Team</b></span></h2>
  <div class="abs team-photo" role="img" aria-label="Group photo of the team"></div>
  <p class="abs team-text body-text" style="line-height:16px"><b>BrightHarbor's company mission is to help small and mid</b>-sized businesses properly plan and align technology with critical business objectives, thereby maximizing.</p>
  <a class="abs more team-more">Read More »</a>
  <div class="abs divider"></div>
</section>

<section>
  <div class="abs card green" style="left:90px"><h3 class="card-head"><span class="ico"><i></i></span><span>IT Consulting <b>Services</b></span></h3><p>Insure that your existing system receives quality service. BrightHarbor will troubleshoot problems, install new software or parts,</p><span class="card-corner"></span></div>
  <div class="abs card dark" style="left:359px"><h3 class="card-head"><span class="ico"><i></i></span><span>IT Service <b>Programs</b></span></h3><p>The certified professionals at BrightHarbor will even set up remote access for staff who work outside of the office,</p><span class="card-corner"></span></div>
  <div class="abs card dark" style="left:626px"><h3 class="card-head"><span class="ico"><i></i></span><span>Security Vulnerability <b>Scan</b></span></h3><p>Assessment services system provide critical information about your system hardware and software....</p><span class="card-corner"></span></div>
</section>

<section>
  <h2 class="abs sec-head col-head" style="left:90px;width:248px"><span class="ico"><i></i></span><span>Featured <b>Services</b></span></h2>
  <ul class="abs list" style="left:90px">
    <li class="link">Nascetur ridiculus musnla fusce feugiat</li><li>Alesda morbi nuncondio, gravida cursus</li><li>Luctus loremnas trisque orciacsem</li><li>Auctor wis duis ultricies</li><li>Situmamet eros dolor onsectetuer</li><li>Mauris dictum magna</li>
  </ul>
  <a class="abs more" style="left:260px;top:1008px">Read More »</a>
  <div class="abs vline" style="left:340px"></div>

  <h2 class="abs sec-head col-head" style="left:360px;width:164px"><span class="ico"><i></i></span><span>New <b>Products</b></span></h2>
  <ul class="abs list" style="left:366px">
    <li class="link">Auctor wis duis ultricies</li><li>Situmamet eros dolor onsectetuer</li><li>Mauris dictum magna</li><li>Utellus dolor, dapibus eget, elementum</li><li>Velcursus eleifend.</li><li>Aliquam erat volutpat duis acturpis.</li>
  </ul>
  <a class="abs more" style="left:517px;top:1008px">Read More »</a>
  <div class="abs vline" style="left:598px"></div>

  <h2 class="abs sec-head col-head" style="left:616px;width:246px;top:854px"><span class="ico" style="background:radial-gradient(circle at 40% 35%,#f7a44a,#2b6cb0)"><i></i></span><span>monitoring &amp; <b style="font-weight:700">security reports</b></span></h2>
  <div class="abs report" role="img" aria-label="Screenshot of a monitoring report with bar chart beside accounting software box"></div>
  <a class="abs more" style="left:790px;top:1008px">Read More »</a>
</section>

<footer>
  <div class="abs footer"></div>
  <div class="abs foot-col" style="left:97px"><h4>BUSINESS CHALLENGES</h4><a>Business Overview</a><a>Choosing an IT Company</a><a>Growing Your Business</a><a>IT Consulting</a><a>&nbsp; - 10 Benefits</a><a>Client Testimonials</a><a>Client Case Studies</a></div>
  <div class="abs foot-col" style="left:287px"><h4>TECHNOLOGY</h4><a>Technology Overview</a><a>Operating Systems</a><a>IT Security</a><a>Business Applications</a><a>Virtualization</a><a>Mobility</a><a>Cloud Computing</a></div>
  <div class="abs foot-col" style="left:454px"><h4>SERVICES</h4><a>Services Overview</a><a>Managed IT Services</a><a>Projects</a><a>Cloud Services</a></div>
  <h2 class="abs testi-head"><span class="ico"><i></i></span><span>Testi<b style="font-weight:700">monial</b></span></h2>
  <blockquote class="abs testi"><b>In the information age of today, one must stay abreast of current</b> technology in order to thrive. New advancements are made daily in dispersing information and collaborative computing, dispersing information.</blockquote>
</footer>
</body>
</html>
```